Design some Business Cards for StartUp

I need an elegant and professional two sides business card. It should be in standard printing format. I already have attached logo. Colors from logo should be used but be careful that are not too vivid and too much colorful because it won't be elegant and professional. I want also to include QR code. Data that must be included (you decide which data are going to be on front page, and which to back page) are the following:

Company name: KRELDA
This text may be included but it is not obligatory: Reliable Web Commerce Advisory Firm, it is some kind of explanation for company name.
Address: Tervosklen 48 (Dorvu), K-17, 60452 Pacirogdo, Menerogtno
Phone: +123 86 20 41 53
Web: www.kreldanet.com
Name: Jelica Marnotic
Title: Founder & CEO
E-mail: jelica.marnotic@kreldanet.com

Attached you can find logo.

```html
<!DOCTYPE html>
<html lang="en">
<head>
<meta charset="utf-8">
<title>KRELDA Business Card</title>
<link href="https://fonts.googleapis.com/css2?family=Open+Sans:wght@400;600&family=Roboto:wght@500&display=swap" rel="stylesheet">
<style>
  :root {
    --bg: #ecebe8;
    --card: #fbfbfb;
    --purple: #8a5e95;
    --salmon: #e7897c;
    --navy: #3d6592;
    --blue: #3d8ac4;
    --ink: #4c4f57;
    --ink-soft: #7a7d85;
    --qr-fill: #e6e4ea;
  }
  * { margin: 0; padding: 0; box-sizing: border-box; }
  html, body { width: 1200px; height: 1023px; overflow: hidden; }
  body {
    background: var(--bg);
    font-family: "Open Sans", Arial, sans-serif;
    position: relative;
  }
  .card {
    position: absolute;
    left: 220px;
    width: 760px;
    height: 434px;
    background: var(--card);
    box-shadow: 0 6px 18px rgba(0,0,0,0.12);
    overflow: hidden;
  }
  .card--front { top: 52px; }
  .card--back { top: 537px; }

  /* front */
  .front__edge {
    position: absolute; left: 0; top: 0; bottom: 0; width: 14px;
    background: var(--navy);
  }
  .front__band {
    position: absolute; left: 0; right: 0; bottom: 0; height: 46px;
    display: flex;
  }
  .front__band span { display: block; height: 100%; }
  .band--purple { background: var(--purple); flex: 1.6; }
  .band--salmon { background: var(--salmon); flex: 1.6; }
  .band--navy { background: var(--navy); flex: 1.3; }
  .band--blue { background: var(--blue); flex: 2.2; }

  .brand {
    position: absolute; left: 170px; top: 140px;
    display: flex; align-items: center; gap: 18px;
  }
  .brand__dot {
    width: 62px; height: 62px; border-radius: 50%;
    background: var(--salmon);
  }
  .brand__name {
    font-family: "Roboto", Arial, sans-serif;
    font-weight: 500;
    font-size: 72px;
    letter-spacing: 2px;
    color: var(--blue);
    line-height: 1;
  }
  .tagline {
    position: absolute; left: 260px; top: 332px;
    font-size: 19px; color: var(--navy);
    letter-spacing: 0.3px;
  }

  /* back */
  .back__side {
    position: absolute; left: 0; top: 0; bottom: 0; width: 96px;
    background: var(--purple);
    display: flex; flex-direction: column; align-items: center;
    padding-top: 40px; gap: 18px;
  }
  .icon {
    width: 30px; height: 30px; border-radius: 50%;
    background: #fff;
    display: flex; align-items: center; justify-content: center;
  }
  .icon svg { width: 16px; height: 16px; }
  .contact {
    position: absolute; left: 118px; top: 40px;
    list-style: none;
    font-size: 16px; color: var(--ink);
  }
  .contact li { height: 30px; line-height: 30px; margin-bottom: 18px; white-space: nowrap; }
  .qr {
    position: absolute; left: 118px; top: 252px;
    width: 112px; height: 112px;
    background: var(--qr-fill);
    border: 6px solid #fff;
    outline: 1px solid #d6d3dc;
  }
  .person {
    position: absolute; right: 64px; top: 250px; text-align: right;
  }
  .person__name {
    font-size: 32px; color: var(--purple); font-weight: 400; line-height: 1.2;
  }
  .person__title {
    font-size: 16px; color: var(--ink-soft); margin-top: 4px; letter-spacing: 0.4px;
  }
  .back__tab {
    position: absolute; right: 40px; bottom: 0;
    width: 260px; height: 42px;
    background: var(--blue);
    border-radius: 6px 6px 0 0;
  }
</style>
</head>
<body>
  <section class="card card--front" aria-label="Card front">
    <div class="front__edge"></div>
    <div class="brand">
      <span class="brand__dot"></span>
      <span class="brand__name">KRELDA</span>
    </div>
    <p class="tagline">Reliable Web Commerce Advisory Firm</p>
    <div class="front__band">
      <span class="band--purple"></span>
      <span class="band--salmon"></span>
      <span class="band--navy"></span>
      <span class="band--blue"></span>
    </div>
  </section>

  <section class="card card--back" aria-label="Card back">
    <div class="back__side">
      <span class="icon"><svg viewBox="0 0 16 16"><path d="M8 1a5 5 0 0 0-5 5c0 4 5 9 5 9s5-5 5-9a5 5 0 0 0-5-5zm0 7a2 2 0 1 1 0-4 2 2 0 0 1 0 4z" fill="#8a5e95"/></svg></span>
      <span class="icon"><svg viewBox="0 0 16 16"><path d="M4 1l3 3-2 2c1 2 3 4 5 5l2-2 3 3-2 3C7 15 1 9 1 3z" fill="#8a5e95"/></svg></span>
      <span class="icon"><svg viewBox="0 0 16 16"><circle cx="8" cy="8" r="6" fill="none" stroke="#8a5e95" stroke-width="1.6"/><path d="M2 8h12M8 2c-3 3-3 9 0 12M8 2c3 3 3 9 0 12" fill="none" stroke="#8a5e95" stroke-width="1.2"/></svg></span>
      <span class="icon"><svg viewBox="0 0 16 16"><rect x="2" y="4" width="12" height="8" fill="none" stroke="#8a5e95" stroke-width="1.6"/><path d="M2 4l6 5 6-5" fill="none" stroke="#8a5e95" stroke-width="1.6"/></svg></span>
    </div>
    <ul class="contact">
      <li>Tervosklen 48 (Dorvu), K-17, 60452 Pacirogdo, Menerogtno</li>
      <li>+123 86 20 41 53</li>
      <li>www.kreldanet.com</li>
      <li>jelica.marnotic@kreldanet.com</li>
    </ul>
    <div class="qr" role="img" aria-label="QR code linking to www.kreldanet.com"></div>
    <div class="person">
      <p class="person__name">Jelica Marnotic</p>
      <p class="person__title">Founder &amp; CEO</p>
    </div>
    <div class="back__tab"></div>
  </section>
</body>
</html>
```